We need a cover designed for our book on parenting. The focus of this book is on the parents, not on the child! We like the idea of this title having a double meaning - insight as in gaining insights into parenting, and "in sight" as in looking inward as parents and how to improve ourselves rather than looking outward to improve our children. We would love for the cover to somehow represent this double meaning. I can upload an excerpt from the book soon over the next few days.
Updates

Reason: We are still reviewing the amazing designs! Thank you so much! :)

Target Market(s)

Parents with kids of any age from babies through adult children.

Requirements
Must have
• Title is: Harbor Parenting
• Subtitle is: Raising Families Through Reflection
• Authors names: Lena Morrow, LCSW Daniel Morrow, Ph.D.

```html
<!DOCTYPE html>
<html lang="en">
<head>
<meta charset="utf-8">
<title>Harbor Parenting – Book Cover</title>
<link rel="stylesheet" href="https://fonts.googleapis.com/css2?family=Arvo:wght@700&family=Arimo:wght@400;700&family=Open+Sans:wght@400&display=swap">
<style>
  :root {
    --page-bg: #ececec;
    --cover-ink: #f6f3ee;
    --sun-gold: #f2a93a;
    --amber: #d9792a;
    --ember: #a8561f;
    --dusk-brown: #4a2a1a;
    --deep-brown: #2e1a12;
    --haze: #c9a27d;
    --label-white: #f4f2ee;
  }
  * { box-sizing: border-box; margin: 0; padding: 0; }
  html, body { width: 1200px; height: 1200px; overflow: hidden; background: var(--page-bg); }
  .spread {
    position: relative; width: 1200px; height: 1200px;
    display: flex; gap: 60px; justify-content: center; align-items: center;
  }
  .cover {
    position: relative; width: 510px; height: 780px; overflow: hidden;
    box-shadow: 0 10px 30px rgba(0,0,0,.22);
  }
  .cover-photo { position: absolute; inset: 0; width: 100%; height: 100%; }

  /* front */
  .front-title {
    position: absolute; top: 120px; left: 0; right: 0;
    font-family: "Arvo", "Rockwell", serif; font-weight: 700;
    color: var(--cover-ink); text-transform: uppercase; text-align: center;
    line-height: 0.98; letter-spacing: 1px;
    text-shadow: 0 2px 6px rgba(60,25,5,.35);
  }
  .front-title .line-one { display: block; font-size: 68px; padding-left: 70px; }
  .front-title .line-two { display: block; font-size: 74px; }
  .front-subtitle {
    position: absolute; right: 40px; top: 450px; width: 420px;
    font-family: "Arvo", "Rockwell", serif; font-weight: 700;
    color: var(--cover-ink); font-size: 46px; line-height: 1.05; text-align: right;
    text-shadow: 0 2px 6px rgba(40,15,5,.4);
  }
  .front-authors {
    position: absolute; left: 0; right: 0; bottom: 58px; text-align: center;
    font-family: "Arimo", Arial, sans-serif; color: var(--cover-ink);
    font-size: 23px;
  }
  .front-authors .amp { font-size: 15px; margin: 0 4px; }

  /* back */
  .back-title {
    position: absolute; top: 80px; left: 0; right: 0; text-align: center;
    font-family: "Arvo", "Rockwell", serif; font-weight: 700;
    color: var(--cover-ink); font-size: 38px; line-height: 1.1;
  }
  .back-blurb {
    position: absolute; top: 190px; left: 40px; right: 40px; text-align: center;
    font-family: "Open Sans", "Myriad Pro", sans-serif; color: var(--cover-ink);
    font-size: 19px; line-height: 1.42;
  }
  .back-label {
    position: absolute; right: 40px; bottom: 60px; width: 190px; height: 130px;
    background: var(--label-white);
  }
</style>
</head>
<body>
<main class="spread">
  <section class="cover cover-front">
    <svg class="cover-photo" viewBox="0 0 510 780" preserveAspectRatio="none" role="img" aria-label="Sunset beach photograph with a meditating hand in the foreground and a family walking along the shore">
      <defs>
        <linearGradient id="frontSky" x1="0" y1="0" x2="0" y2="1">
          <stop offset="0" stop-color="var(--ember)"/>
          <stop offset="0.22" stop-color="var(--sun-gold)"/>
          <stop offset="0.45" stop-color="var(--amber)"/>
          <stop offset="0.58" stop-color="var(--haze)"/>
          <stop offset="0.72" stop-color="var(--ember)"/>
          <stop offset="1" stop-color="var(--deep-brown)"/>
        </linearGradient>
        <radialGradient id="frontSun" cx="0.82" cy="0.04" r="0.35">
          <stop offset="0" stop-color="#fff6e0" stop-opacity="0.9"/>
          <stop offset="1" stop-color="#fff6e0" stop-opacity="0"/>
        </radialGradient>
      </defs>
      <rect width="510" height="780" fill="url(#frontSky)"/>
      <rect width="510" height="780" fill="url(#frontSun)"/>
    </svg>
    <h1 class="front-title"><span class="line-one">Harbor</span><span class="line-two">Parenting</span></h1>
    <p class="front-subtitle">Raising Families Through Reflection</p>
    <p class="front-authors">Lena Morrow, LCSW<span class="amp">&amp;</span>Daniel Morrow, Ph.D</p>
  </section>

  <section class="cover cover-back">
    <svg class="cover-photo" viewBox="0 0 510 780" preserveAspectRatio="none" role="img" aria-label="Blurred sunset shoreline with a small silhouetted family walking hand in hand">
      <defs>
        <linearGradient id="backSky" x1="0" y1="0" x2="0" y2="1">
          <stop offset="0" stop-color="var(--amber)"/>
          <stop offset="0.3" stop-color="var(--ember)"/>
          <stop offset="0.5" stop-color="var(--haze)"/>
          <stop offset="0.62" stop-color="var(--ember)"/>
          <stop offset="1" stop-color="var(--dusk-brown)"/>
        </linearGradient>
      </defs>
      <rect width="510" height="780" fill="url(#backSky)"/>
    </svg>
    <h2 class="back-title">Raising Families<br>Through Reflection</h2>
    <p class="back-blurb">We need a cover designed for our book on parenting. The focus of this book is on the parents, not on the child! We like the idea of this title having a double meaning - insight as in gaining insights into parenting, and "in sight" as in looking inward as parents and how to improve ourselves rather than looking outward to improve our children. We would love for the cover to somehow represent this double meaning. I can upload an excerpt from the book soon over the next few days.</p>
    <div class="back-label"></div>
  </section>
</main>
</body>
</html>
```